Painting Contractor Business Card Design

We are looking for a cool, bold, modern, polished, business card design. We are a high-end residential painting contractor. Please incorporate our logo and keep with our green/black color scheme. We are interested in seeing 2-sided and 1-sided options. Thank you very much!

Industry/Entity Type

Business

Contact Information for Business Card

Info for the card:
Dale Ormsby
mobile 206-555-0193
email dale@tallowbrookpainting.net
web www.tallowbrookpainting.net

```html
<!DOCTYPE html>
<html lang="en">
<head>
<meta charset="utf-8">
<title>Tallowbrook Painting – Business Card</title>
<link href="https://fonts.googleapis.com/css2?family=Montserrat:wght@700&family=Questrial&display=swap" rel="stylesheet">
<style>
  :root {
    --backdrop: #333333;
    --card-white: #ffffff;
    --ink: #1d1d1d;
    --brand-green: #2eaa62;
    --navy: #0f4677;
    --mid-blue: #1a73b8;
    --contact-white: #ffffff;
  }
  html, body {
    margin: 0;
    width: 1200px;
    height: 840px;
    overflow: hidden;
    background: var(--backdrop);
  }
  .card {
    position: absolute;
    left: 48px;
    top: 106px;
    width: 1105px;
    height: 628px;
    background: var(--card-white);
    border-radius: 96px 0 96px 0;
    overflow: hidden;
  }
  .card-band {
    position: absolute;
    inset: 0;
    width: 100%;
    height: 100%;
  }
  .brand {
    position: absolute;
    left: 242px;
    top: 84px;
    display: flex;
    align-items: center;
    gap: 26px;
  }
  .brand-square {
    width: 150px;
    height: 150px;
    background: var(--brand-green);
  }
  .brand-name {
    margin: 0;
    font-family: "Montserrat", sans-serif;
    font-weight: 700;
    font-size: 62px;
    line-height: 1.08;
    color: var(--ink);
    letter-spacing: 0.5px;
  }
  .contact {
    position: absolute;
    right: 32px;
    top: 418px;
    text-align: right;
    color: var(--contact-white);
  }
  .contact-name {
    margin: 0 44px 14px 0;
    font-family: "Montserrat", sans-serif;
    font-weight: 700;
    font-size: 30px;
    letter-spacing: 0.5px;
  }
  .contact-list {
    list-style: none;
    margin: 0;
    padding: 0;
    font-family: "Questrial", sans-serif;
    font-size: 26px;
  }
  .contact-list li {
    display: flex;
    justify-content: flex-end;
    align-items: center;
    gap: 12px;
    height: 42px;
  }
  .contact-icon {
    width: 22px;
    height: 22px;
    flex: none;
  }
</style>
</head>
<body>
  <div class="card">
    <svg class="card-band" viewBox="0 0 1105 628" preserveAspectRatio="none" role="img" aria-label="Decorative paint-stroke artwork in blue and green">
      <defs>
        <linearGradient id="band-gradient" x1="0" y1="0" x2="1" y2="0">
          <stop offset="0" stop-color="var(--navy)"/>
          <stop offset="0.3" stop-color="var(--mid-blue)"/>
          <stop offset="0.58" stop-color="var(--brand-green)"/>
          <stop offset="1" stop-color="var(--brand-green)"/>
        </linearGradient>
      </defs>
      <polygon points="0,400 1105,190 1105,628 0,628" fill="url(#band-gradient)"/>
    </svg>

    <div class="brand">
      <div class="brand-square"></div>
      <p class="brand-name">TALLOWBROOK<br>PAINTING</p>
    </div>

    <div class="contact">
      <p class="contact-name">DALE ORMSBY</p>
      <ul class="contact-list">
        <li>206-555-0193
          <svg class="contact-icon" viewBox="0 0 24 24" aria-hidden="true"><path fill="#1d1d1d" d="M3 8 Q12 2 21 8 L19 11 L16 10 L16 8 Q12 6.5 8 8 L8 10 L5 11 Z M6 12 L18 12 L20 20 L4 20 Z"/><circle cx="12" cy="16" r="2" fill="#ffffff"/></svg>
        </li>
        <li>dale@tallowbrookpainting.net
          <svg class="contact-icon" viewBox="0 0 24 24" aria-hidden="true"><rect x="2" y="5" width="20" height="14" fill="#1d1d1d"/><path d="M2 5 L12 13 L22 5" fill="none" stroke="#ffffff" stroke-width="1.5"/></svg>
        </li>
        <li>www.tallowbrookpainting.net
          <svg class="contact-icon" viewBox="0 0 24 24" aria-hidden="true"><circle cx="12" cy="12" r="10" fill="#1d1d1d"/><path d="M4 9 Q12 13 20 9 M4 15 Q12 11 20 15 M12 2 Q7 12 12 22 M12 2 Q17 12 12 22" fill="none" stroke="#ffffff" stroke-width="1.2"/></svg>
        </li>
      </ul>
    </div>
  </div>
</body>
</html>
```